"Swoon Beneath Lanterns" E-Book Cover Design

We're looking for a electronic book cover with a picture of a ninja side-kicking towards the viewer, holding roses in one hand. We'd like the ninja to be animated or cartoon in form.
At the top, in big letters is the title: "Swoon Beneath Lanterns."
Beneath that, as a smaller subtitle: "60 Heart-Racing Outing Plans."
At the bottom, the author's name: "Maribel Okonkwo."
We've attached a file with the type of ninja image we're looking for and the background coloring. This image is copyrighted, and we do NOT own the rights to it. It's just to give a visual example of what we're looking for.
We're not sure what sort of background we'd like. Please feel free to experiment.
Thank you for your interest!
Romantic couples of all ages, from around 20 on up. (English speaking, mostly Pagero users)
Electronic

```html
<!DOCTYPE html>
<html lang="en">
<head>
<meta charset="utf-8">
<title>Swoon Beneath Lanterns — Cover Options</title>
<link rel="stylesheet" href="https://fonts.googleapis.com/css2?family=Big+Shoulders+Display:wght@200;300&family=Cinzel:wght@400;600&family=Open+Sans:wght@400&display=swap">
<style>
  :root {
    --board: #5b5b5b;
    --paper: #ffffff;
    --ink: #000000;
    --lime: #c8dc7a;
    --leaf: #3ab54a;
    --emerald: #22b06a;
    --blush: #f4a3a8;
    --aqua: #7fcfda;
    --butter: #fcefc0;
    --faint: #e6e6e6;
  }
  * { margin: 0; padding: 0; box-sizing: border-box; }
  html, body { width: 1200px; height: 447px; overflow: hidden; background: var(--board); }
  .board { position: relative; width: 1200px; height: 447px; }

  .cover {
    position: absolute;
    width: 266px;
    height: 400px;
    background: var(--paper);
    overflow: hidden;
  }
  .cover--geometric { left: 9px;   top: 27px; }
  .cover--bubbles   { left: 313px; top: 27px; }
  .cover--outline   { left: 626px; top: 30px; }
  .cover--lime      { left: 927px; top: 25px; }

  .backdrop { position: absolute; inset: 0; width: 100%; height: 100%; }

  .title {
    position: absolute;
    left: 16px;
    right: 14px;
    top: 40px;
    display: flex;
    align-items: flex-end;
    white-space: nowrap;
    font-family: "Big Shoulders Display", sans-serif;
    font-weight: 300;
    color: var(--ink);
    line-height: 0.8;
    text-transform: uppercase;
  }
  .title__lead { font-size: 72px; font-weight: 300; letter-spacing: -2px; }
  .title__link {
    font-family: "Open Sans", sans-serif;
    font-size: 7px;
    text-transform: lowercase;
    margin: 0 2px 1px 2px;
  }
  .title__tail { font-size: 33px; font-weight: 200; letter-spacing: 0; }

  .subtitle {
    position: absolute;
    left: 0; right: 0;
    top: 128px;
    padding-left: 20px;
    font-family: "Cinzel", serif;
    font-size: 6.5px;
    letter-spacing: 2.2px;
    white-space: nowrap;
    color: var(--ink);
  }

  .hero {
    position: absolute;
    left: 52px;
    top: 175px;
    width: 150px;
    height: 100px;
    border-radius: 14px;
    background: radial-gradient(circle at 18% 22%, #a3262a 0 12%, transparent 13%),
                linear-gradient(135deg, #1a1a1a, #000000);
  }

  .author {
    position: absolute;
    left: 0; right: 0;
    top: 352px;
    text-align: center;
    font-family: "Cinzel", serif;
    font-size: 7px;
    font-weight: 600;
    letter-spacing: 2px;
    white-space: nowrap;
    color: var(--ink);
  }
  .author--marked span {
    background: linear-gradient(transparent 55%, var(--lime) 55%);
  }
</style>
</head>
<body>
<main class="board">

  <section class="cover cover--geometric">
    <svg class="backdrop" viewBox="0 0 295 445" preserveAspectRatio="none" aria-hidden="true">
      <circle cx="155" cy="370" r="155" fill="var(--lime)"/>
      <polygon points="270,240 165,270 55,395 90,445 120,445 155,330 295,300" fill="var(--paper)"/>
      <polygon points="0,125 145,103 175,130 0,160" fill="var(--leaf)" opacity="0.85"/>
      <polygon points="215,120 242,132 122,445 95,445" fill="var(--leaf)" opacity="0.85"/>
      <polygon points="0,395 230,345 238,362 0,420" fill="var(--leaf)" opacity="0.85"/>
      <polygon points="270,20 295,40 295,60 250,40 170,90 160,70" fill="var(--emerald)"/>
      <polygon points="150,195 270,200 300,300 230,380 110,375 80,280" fill="none" stroke="var(--emerald)" stroke-width="2.5"/>
      <polygon points="180,80 270,70 295,180 250,260 175,240 165,150" fill="none" stroke="var(--emerald)" stroke-width="1.5"/>
    </svg>
    <h1 class="title"><span class="title__lead">Swoon</span><span class="title__link">beneath</span><span class="title__tail">Lanterns</span></h1>
    <p class="subtitle">60 Heart-Racing Outing Plans</p>
    <div class="hero" role="img" aria-label="Cartoon ninja side-kicking toward the viewer, holding a red rose"></div>
    <p class="author">Maribel Okonkwo</p>
  </section>

  <section class="cover cover--bubbles">
    <svg class="backdrop" viewBox="0 0 295 445" preserveAspectRatio="none" aria-hidden="true">
      <circle cx="290" cy="170" r="115" fill="var(--aqua)"/>
      <circle cx="62" cy="410" r="135" fill="var(--butter)"/>
      <circle cx="82" cy="232" r="75" fill="var(--blush)" opacity="0.9"/>
      <circle cx="197" cy="450" r="115" fill="var(--lime)" opacity="0.95"/>
    </svg>
    <h1 class="title"><span class="title__lead">Swoon</span><span class="title__link">beneath</span><span class="title__tail">Lanterns</span></h1>
    <p class="subtitle">60 Heart-Racing Outing Plans</p>
    <div class="hero" role="img" aria-label="Cartoon ninja side-kicking toward the viewer, holding a red rose"></div>
    <p class="author">Maribel Okonkwo</p>
  </section>

  <section class="cover cover--outline">
    <svg class="backdrop" viewBox="0 0 295 445" preserveAspectRatio="none" aria-hidden="true">
      <circle cx="155" cy="370" r="155" fill="none" stroke="var(--faint)" stroke-width="1" stroke-dasharray="3 3"/>
      <polyline points="270,240 165,270 55,395 90,445" fill="none" stroke="var(--faint)" stroke-width="1" stroke-dasharray="3 3"/>
      <polyline points="120,445 155,330 295,300" fill="none" stroke="var(--faint)" stroke-width="1" stroke-dasharray="3 3"/>
    </svg>
    <h1 class="title"><span class="title__lead">Swoon</span><span class="title__link">beneath</span><span class="title__tail">Lanterns</span></h1>
    <p class="subtitle">60 Heart-Racing Outing Plans</p>
    <div class="hero" role="img" aria-label="Cartoon ninja side-kicking toward the viewer, holding a red rose"></div>
    <p class="author author--marked"><span>Maribel Okonkwo</span></p>
  </section>

  <section class="cover cover--lime">
    <svg class="backdrop" viewBox="0 0 295 445" preserveAspectRatio="none" aria-hidden="true">
      <circle cx="155" cy="370" r="170" fill="var(--lime)"/>
      <polygon points="270,240 165,270 55,395 90,445 120,445 155,330 295,300" fill="var(--paper)"/>
    </svg>
    <h1 class="title"><span class="title__lead">Swoon</span><span class="title__link">beneath</span><span class="title__tail">Lanterns</span></h1>
    <p class="subtitle">60 Heart-Racing Outing Plans</p>
    <div class="hero" role="img" aria-label="Cartoon ninja side-kicking toward the viewer, holding a red rose"></div>
    <p class="author">Maribel Okonkwo</p>
  </section>

</main>
</body>
</html>
```